Business Card for my New Brokerage

Looking to get a business card design for my new Real Estate Brokerage.
I want it with Picture, Phone Number, Email, Website, Office Address
Name and Designation. Please add logo too.

Target Market(s)

Real Estate Investors or Home Buyers

Industry/Entity Type

Real Estate

Contact Information for Business Card

Name, Email, Phone Number, website, email, office address

Colors
EB3D1F
EC4F4E
F09395
F8D3D4
FCEDEE

Requirements
Must have
• Minimalistic, Clean, Modern, Photo
Nice to have
• White and Red Colors

```html
<!DOCTYPE html>
<html lang="en">
<head>
<meta charset="utf-8">
<title>Brokerage Business Card</title>
<link rel="stylesheet" href="https://fonts.googleapis.com/css2?family=Lato:wght@400;700;900&display=swap">
<style>
  :root {
    --page-bg: #e7e4e2;
    --brand-red: #de0000;
    --frost-light: #f7f4f3;
    --frost-mid: #e4dcda;
    --frost-warm: #eadad8;
    --gold-light: #f7e27a;
    --gold-deep: #d1a629;
    --text-light: #ffffff;
  }
  * { box-sizing: border-box; margin: 0; padding: 0; }
  html, body {
    width: 1200px;
    height: 900px;
    overflow: hidden;
    background: var(--page-bg);
    font-family: "Lato", sans-serif;
  }
  .business-card {
    position: absolute;
    left: 120px;
    top: 153px;
    width: 960px;
    height: 594px;
    overflow: hidden;
    background: linear-gradient(135deg, var(--frost-light) 0%, var(--frost-warm) 45%, var(--frost-mid) 70%, var(--frost-light) 100%);
    box-shadow: 0 18px 40px rgba(0,0,0,0.18);
  }
  .card-shapes {
    position: absolute;
    inset: 0;
  }
  .contact-panel {
    position: absolute;
    left: 59px;
    top: 68px;
    color: var(--text-light);
  }
  .agent-name {
    font-weight: 700;
    font-size: 39px;
    line-height: 1.05;
    letter-spacing: -0.3px;
  }
  .agent-title {
    font-weight: 400;
    font-size: 28px;
    line-height: 1.2;
  }
  .office-address {
    margin-top: 36px;
    font-size: 28px;
    line-height: 35px;
    font-style: normal;
  }
  .contact-list {
    list-style: none;
    margin-top: 22px;
  }
  .contact-item {
    display: flex;
    align-items: center;
    gap: 10px;
    font-size: 28px;
    line-height: 37px;
  }
  .contact-icon {
    width: 28px;
    height: 28px;
    flex: none;
  }
  .brand-name {
    position: absolute;
    left: 470px;
    top: 388px;
    width: 440px;
    text-align: center;
    color: var(--brand-red);
    font-weight: 900;
    font-size: 52px;
    letter-spacing: 1px;
  }
</style>
</head>
<body>
  <section class="business-card">
    <svg class="card-shapes" viewBox="0 0 960 594" width="960" height="594">
      <defs>
        <linearGradient id="gold-strip" x1="0" y1="0" x2="1" y2="1">
          <stop offset="0" stop-color="var(--gold-light)"/>
          <stop offset="0.5" stop-color="var(--gold-deep)"/>
          <stop offset="1" stop-color="var(--gold-light)"/>
        </linearGradient>
      </defs>
      <polygon class="red-panel" points="0,0 697,0 318,594 0,594" fill="var(--brand-red)"/>
      <polygon class="sparkle-border" role="img" aria-label="Row of gold sparkle ornaments along the diagonal edge"
               points="680,0 697,0 318,594 301,594" fill="url(#gold-strip)" opacity="0.85"/>
    </svg>

    <div class="contact-panel">
      <h1 class="agent-name">DANIEL HARPER</h1>
      <p class="agent-title">Managing Director</p>
      <address class="office-address">
        18, Harbor View Lane<br>
        Brookfield, 40218
      </address>
      <ul class="contact-list">
        <li class="contact-item">
          <svg class="contact-icon" viewBox="0 0 24 24" fill="none" stroke="#fff" stroke-width="2" stroke-linecap="round" stroke-linejoin="round">
            <path d="M22 16.9v3a2 2 0 0 1-2.2 2 19.8 19.8 0 0 1-8.6-3.1 19.5 19.5 0 0 1-6-6A19.8 19.8 0 0 1 2.1 4.2 2 2 0 0 1 4.1 2h3a2 2 0 0 1 2 1.7c.1 1 .4 1.9.7 2.8a2 2 0 0 1-.5 2.1L8 9.9a16 16 0 0 0 6 6l1.3-1.3a2 2 0 0 1 2.1-.4c.9.3 1.8.6 2.8.7a2 2 0 0 1 1.7 2z"/>
          </svg>
          <span>555-010 482 731</span>
        </li>
        <li class="contact-item">
          <svg class="contact-icon" viewBox="0 0 24 24" fill="none" stroke="#fff" stroke-width="2" stroke-linejoin="round">
            <rect x="2" y="5" width="20" height="14"/>
            <path d="M2 5l10 8 10-8M2 19l7-7M22 19l-7-7"/>
          </svg>
          <span>info@lumenrealty.co</span>
        </li>
        <li class="contact-item">
          <svg class="contact-icon" viewBox="0 0 24 24" fill="none" stroke="#fff" stroke-width="2">
            <circle cx="12" cy="12" r="10"/>
            <ellipse cx="12" cy="12" rx="4.5" ry="10"/>
            <path d="M2 12h20M4 7h16M4 17h16"/>
          </svg>
          <span>www.lumenrealty.co</span>
        </li>
      </ul>
    </div>

    <p class="brand-name">LUMEN REALTY</p>
  </section>
</body>
</html>
```